Resume: Professional Marketer seeking to impress potential recruiters with my skills & experience

Create a marketing esque style CV. I'm an outgoing, driven marketing with years of experience. I'm looking for a new senior role. My CV should look professional, but with elements of creativity and be a little bold. It should stand out amongst all the other CVs being submitted for a role. Check out my crewbase profile here: https://www.crewbase.example/in/marisol-tovrek-58210394/ I would like to include a photo with the design, as a subtle element of the design.

Target Market(s)

Recruiters, Headhunters

Industry/Entity Type

Marketing

Font styles to use
Sans Serif

Requirements
Must have
• Easy to read sections, with enough detail for a recruiter to understand my experience.
Nice to have
• Graphics, icons etc to represent experience

```html
<!DOCTYPE html>
<html lang="en">
<head>
<meta charset="utf-8">
<title>Marisol Tovrek – Marketing CV</title>
<link rel="stylesheet" href="https://fonts.googleapis.com/css2?family=Titillium+Web:ital,wght@0,400;0,700;1,700&family=Open+Sans:ital,wght@0,400;0,700;1,400&display=swap">
<style>
:root{
  --navy:#1e3a6e;
  --navy-dark:#15294f;
  --tint:#c9d6e4;
  --tint-soft:#e7edf4;
  --ink:#2b2f36;
  --tick:#2f7a3a;
  --stage:#e6e6e4;
}
*{box-sizing:border-box;margin:0;padding:0}
html,body{width:1200px;height:1200px;overflow:hidden;background:var(--stage)}
body{position:relative;font-family:"Open Sans",Arial,sans-serif;color:var(--ink)}
.page{position:absolute;width:274px;height:356px;background:#fff;overflow:hidden;box-shadow:0 2px 6px rgba(0,0,0,.18)}
.p1{left:317px;top:44px}.p2{left:609px;top:44px}
.p3{left:317px;top:422px}.p4{left:609px;top:422px}
.p5{left:317px;top:800px}.p6{left:609px;top:800px}

/* header on page one */
.hero-bg{position:absolute;left:0;top:0}
.city-photo{position:absolute;left:0;top:0;width:112px;height:64px;background:linear-gradient(135deg,#9fb6d3,#dfe7f1 55%,#7d98bd)}
.portrait{position:absolute;left:210px;top:8px;width:64px;height:142px;background:linear-gradient(180deg,#e9dcc9,#c9a988 45%,#3a3432)}
.name{position:absolute;left:116px;top:22px;font-family:"Titillium Web",sans-serif;font-weight:700;font-size:11.5px;color:var(--navy);letter-spacing:.2px;line-height:1}
.name-rule{position:absolute;left:116px;top:35px;width:84px;height:1px;background:var(--navy)}
.contact-line{position:absolute;left:116px;top:38px;font-size:5.4px;font-style:italic;color:var(--navy)}
.intro{position:absolute;left:10px;top:56px;width:196px;color:#fff}
.intro p{font-size:3.6px;line-height:1.22;margin-bottom:3px}

.section-title{font-family:"Titillium Web",sans-serif;font-style:italic;font-weight:700;font-size:7.6px;color:var(--navy);display:flex;align-items:center;gap:4px;line-height:1}
.section-title::after{content:"";flex:1;height:1px;background:var(--navy)}
.intro .section-title{color:#fff;margin-bottom:3px}
.intro .section-title::after{display:none}

.employment{position:absolute;left:8px;top:160px;width:258px}
.employment .section-title{margin-bottom:4px}
table{border-collapse:collapse;width:100%}
.record th{background:var(--navy);color:#fff;font-size:3.6px;line-height:1.2;text-align:left;padding:1px 2px}
.record td{font-size:3.3px;line-height:1.1;padding:0 2px;vertical-align:middle;height:10.2px}
.record tr:nth-child(even) td{background:var(--tint-soft)}

/* skills */
.block{position:absolute;left:10px;width:254px}
.skills{display:grid;grid-template-columns:repeat(3,1fr);border:1px solid var(--navy);margin-top:5px}
.skills span{font-size:3.9px;padding:2px 3px 2px 4px;display:flex;align-items:center;gap:5px;border-bottom:1px solid #fff}
.skills span:nth-child(6n+1),.skills span:nth-child(6n+2),.skills span:nth-child(6n+3){background:var(--tint-soft)}
.skills span::before{content:"\2713";color:var(--tick);font-weight:700;font-size:4.4px}

/* role blocks */
.role{border:1px solid var(--navy);margin-bottom:5px}
.role td{font-size:3.5px;line-height:1.28;padding:1.6px 2px;vertical-align:top}
.role td.label{width:50px;border-right:1px solid var(--navy)}
.role tr.head td{background:var(--tint);border-bottom:1px solid var(--navy)}
.role tr.head td.label{font-weight:700}
.role ol{list-style:none}
.role li{padding-left:4px;text-indent:-4px}
.role p{margin-bottom:3px}
.gap td{height:6px}

/* closing page */
.pill{position:absolute;left:8px;width:258px;height:9px;border-radius:5px;background:var(--navy);color:#fff;font-size:3.7px;font-style:italic;display:flex;align-items:center;justify-content:center;gap:3px}
.sub{font-size:4.2px;color:var(--navy);margin:6px 0 3px}
.quals th{background:var(--navy);color:#fff;font-size:3.5px;text-align:left;padding:1px 3px}
.quals td{font-size:3.3px;line-height:1.2;padding:1.6px 3px;background:var(--tint-soft);vertical-align:top;height:13px}
.footer{position:absolute;left:0;bottom:0;width:274px;height:17px;background:var(--navy);color:#d9e2ee;font-size:3.8px;letter-spacing:1.4px;display:flex;align-items:center;justify-content:center}
</style>
</head>
<body>

<!-- Page 1 -->
<section class="page p1">
  <div class="city-photo" role="img" aria-label="Photo of glass office towers"></div>
  <div class="portrait" role="img" aria-label="Portrait photo of Marisol Tovrek"></div>
  <svg class="hero-bg" width="274" height="160" viewBox="0 0 274 160" aria-hidden="true">
    <path d="M0 52 H176 Q208 52 213 90 L219 144 Q110 156 0 150 Z" fill="var(--navy)"/>
  </svg>
  <div class="name">MARISOL TOVREK</div>
  <div class="name-rule"></div>
  <div class="contact-line">Bayview Heights NSW 0400 118 263</div>
  <div class="intro">
    <h2 class="section-title">INTRODUCTION</h2>
    <p>I am a passionate direct marketer of 15+ years experience in Australia, plus key roles in startup organisations in London and New York.</p>
    <p>I am a talented consumer marketer with strong commercial and business acumen. I played a fundamental role in the growth of CoverWell Pty Ltd, to become the number one direct life insurance brand in Australia.</p>
    <p>As a strategic marketer, my strengths lie in analytical thinking and the ability to translate marketing and sales activity into commercial modeling, and ultimately profitability.</p>
    <p>I am a talented professional with the drive to succeed. I have benefited from working alongside exceptional people, who have helped me develop personally, and as a leader. My goals are to engage with as many strategic and intellectual minds as possible, and to help others develop to achieve theirs.</p>
  </div>
  <div class="employment">
    <h2 class="section-title">EMPLOYMENT RECORD (LAST 15 YEARS)</h2>
    <table class="record">
      <tr><th style="width:16%">Dates</th><th style="width:46%">Role</th><th>Organisation</th></tr>
      <tr><td>May 2016<br>to Current</td><td>Marketing Strategy Consultant</td><td>Clients include Roadside Journal, Alpen Re,<br>Marlow Studio, Supper Club Co</td></tr>
      <tr><td>January 2011<br>to Current</td><td>Marketer and Business Development</td><td>Reid Calloway Photography</td></tr>
      <tr><td>August 2015<br>to May 2016</td><td>Career break</td><td></td></tr>
      <tr><td>April 2015<br>to August 2015</td><td>Head of Marketing</td><td>Meridian Life Partners (US)<br>Kindred Life (life insurance brand)</td></tr>
      <tr><td>August 2014<br>to April 2015</td><td>Maternity Leave – to my son</td><td></td></tr>
      <tr><td>March 2014<br>to August 2014</td><td>General Manager Marketing and Business Operations</td><td>Meridian Life Partners (UK)<br>Vantage Life (life insurance brand)</td></tr>
      <tr><td>May 2013<br>to April 2014</td><td>Career Break</td><td></td></tr>
      <tr><td>October 2013</td><td>Consultant – New Business Proposal</td><td>Brightwater Administration Services Pty Limited</td></tr>
      <tr><td>December 2012<br>to May 2013</td><td>Commercial &amp; MIS Manager</td><td>Halden Life Limited</td></tr>
      <tr><td>July 2012<br>to December 2012</td><td>Head of Marketing Operations – Acquisition and Retention</td><td>Halden Life Limited</td></tr>
      <tr><td>October 2010<br>to July 2012</td><td>P&amp;L / Brand Manager – CoverWell</td><td>Halden Life Limited</td></tr>
      <tr><td>January 2010<br>to October 2010</td><td>Product Portfolio Marketing Manager – CoverWell</td><td>Halden Life Limited<br>(previously HARBOUR)</td></tr>
      <tr><td>January 2008<br>to October 2010</td><td>Marketing Manager – CoverWell</td><td>Halden Life Limited (CoverWell Pty Limited<br>was acquired by Halden Life in September 2008)</td></tr>
      <tr><td>February 2007<br>to December 2007</td><td>Database and Retention Strategy Manager</td><td>CoverWell Pty Limited<br>Melbourne Office relocation</td></tr>
      <tr><td>July 2004<br>to January 2007</td><td>Direct Marketing Specialist</td><td>CoverWell Pty Limited</td></tr>
      <tr><td>April 2002<br>to June 2004</td><td>Acquisition and Database Marketing Manager – Japan</td><td>Rewardco Pty Ltd<br>(currently known as Postline Pty Ltd)</td></tr>
    </table>
  </div>
</section>

<!-- Page 2 -->
<section class="page p2">
  <div class="block" style="top:12px">
    <h2 class="section-title">KEY SKILLS AND EXPERIENCE</h2>
    <div class="skills">
      <span>Advertising</span><span>Digital Marketing</span><span>Media Planning</span>
      <span>Branding</span><span>Distribution</span><span>People Management</span>
      <span>Budgeting &amp; Forecasting</span><span>Direct Marketing</span><span>Product Development</span>
      <span>Business Analysis</span><span>Executive Reporting</span><span>P&amp;L Responsibility</span>
      <span>Call Centres</span><span>Financial Modelling</span><span>Retention</span>
      <span>Customer Acquisition</span><span>Lead Generation</span><span>Sales</span>
      <span>Customer Retention</span><span>Marketing Analysis</span><span>Strategy Development</span>
      <span>Copy Writing</span><span>Marketing</span><span>Stakeholder Management</span>
    </div>
  </div>
  <div class="block" style="top:124px">
    <h2 class="section-title">EXPERIENCE &amp; RESPONSIBILITIES FOR EACH ROLE</h2>
    <div style="height:5px"></div>
    <table class="role">
      <tr class="head"><td class="label">May 2016<br>to May 2018</td><td>Marketing Strategy Consultant</td></tr>
      <tr><td class="label">Role responsibilities:</td><td><p>Working with businesses – large and small – to drive and execute change in order to achieve their corporate and financial goals.</p><p>Consulting services include: developing and improving new and existing marketing strategy, product strategy, and customer experience. Building their business and financial positions through understanding the sales process and customer path to purchase, implementing process improvement, and through improved forecasting, and cost and budget management.</p></td></tr>
      <tr><td class="label">Reporting to:</td><td><p>Primary key stakeholders are the clients management team, their teams, agencies, and suppliers.</p></td></tr>
      <tr><td class="label">Key Relationships:</td><td>Clients include Roadside Journal, Alpen Re, Marlow Studio, Supper Club Co, Healthwise.</td></tr>
    </table>
    <table class="role">
      <tr class="head"><td class="label">April 2015<br>to August 2015</td><td>Head of Marketing<br>Meridian Life Partners (US) – Kindred Life, consumer life insurance brand</td></tr>
      <tr><td class="label">Role responsibilities:</td><td>
        <p>The overarching objectives of the Head of Marketing role were to:</p>
        <ol><li>1. To prepare Kindred Life for the launch of the Direct Life Insurance brand.</li>
        <li>2. To achieve the operational new business plan (sales units, revenue &amp; appropriate acquisition expenditure), with the Head of Sales.</li>
        <li>3. To recruit Chief Marketing Officer to replace me (upon the planned move to Meridian Life Partners (UK); as the role of Chief Marketing Officer, UK).</li></ol>
        <p style="margin-top:3px">The objectives of the Head of Marketing:</p>
        <ol><li>4. To develop and execute the Marketing strategy for Kindred Life</li>
        <li>5. To develop all Marketing materials for the launch, including direct response TV commercials and website</li>
        <li>6. To develop TV media plan and partner with a New York Media Agency</li>
        <li>7. To develop the Acquisition Plan to meet the Year 1 Sales unit targets, within budget</li></ol>
      </td></tr>
    </table>
  </div>
</section>

<!-- Page 3 -->
<section class="page p3">
  <div class="block" style="top:10px">
    <table class="role">
      <tr><td class="label"></td><td>
        <ol><li>8. To manage the marketing budget to deliver the lead, acquisition, brand, digital, and communications objectives of the organisation</li>
        <li>9. To take ownership of the annual acquisition budget setting process</li>
        <li>10. To ensure the customer retention strategy is in place to achieve the financial targets for customer retention</li>
        <li>11. To manage the Marketing project plan to deadline, given the critical path predominantly marketing</li>
        <li>12. To develop relationships and engage with all external business partners; including, Marketing Suppliers, Call Centre Operators, the Insurer and their Consultants, Printers and Mail houses, Telephony providers, Recruiters, and Legal Counsel</li>
        <li>13. Participate in decision making and strategic discussion for broad business planning, projects, investment decisions and strategy</li></ol>
      </td></tr>
      <tr class="gap"><td class="label"></td><td></td></tr>
      <tr><td class="label">Reporting to:</td><td>Reporting to: CEO, Meridian Life Partners US</td></tr>
      <tr><td class="label">Key Relationships:</td><td><p>Key stakeholder relationships with;<br>Five owners of Meridian Life Partners, Alpen Re US (a reinsurer), and NSLI (the insurance company).</p><p>Being a start up, whilst strategic, this role was naturally 'sleeves rolled up and hands on'.</p><p>The role in the US was a 12 month contract, before a planned return to Meridian Life Partners (UK) as the Chief Marketing Officer. Unfortunately, this did not happen, as my family faced a serious illness in August 2015, and I returned home in November 2015.</p></td></tr>
    </table>
    <table class="role">
      <tr class="head"><td class="label">March 2014<br>to August 2014</td><td>Head of Marketing &amp; General Manager - Business Operations<br>Meridian Life Partners (UK) - Vantage Life, consumer life insurance brand<br>This role was a 3 month contract.</td></tr>
      <tr><td class="label">Role responsibilities:</td><td>
        <p>The overarching objectives of the 3 month relocation to London were to:</p>
        <ol><li>1. To prepare MLP UK for the launch of the Direct Life Insurance brand.</li>
        <li>2. To leave the MLP UK in a prepared position for the CEO &amp; MLP team to successfully launch the brand to the agreed timeline.</li></ol>
        <p style="margin-top:3px">The primary objectives of the General Manager Marketing &amp; Business Operations:</p>
        <ol><li>1. To obtain financial services license for MLP (Direct Authorisation &amp; Appointed Rep Status)</li>
        <li>2. To establish the Sales Call Centre front end &amp; lead management processes</li>
        <li>3. To develop the Acquisition Plan to meet the Year 1 Sales unit targets, within budget</li>
        <li>4. To shortlist Creative Agencies for selection by the CEO, UK</li>
        <li>5. To shortlist Marketing roles and Support roles for selection by the CEO, UK</li>
        <li>6. To develop the project plan, and to understand and outline the critical path</li>
        <li>7. Develop relationships and pursue engagement with all external business partners; including, Marketing Suppliers, Call Centre Operators, the Insurer and their Consultants, Printers and Mail houses, Telephony providers, Recruiters, Banks, external Legal Counsel, Compliance Consultants, IT providers.</li>
        <li>8. General administration of a start up company overseas</li></ol>
      </td></tr>
      <tr><td class="label">Reporting to:</td><td>Reporting to: Group CEO, Meridian Life Partners</td></tr>
      <tr><td class="label">Key Relationships:</td><td>Key stakeholder relationships with;<br>Five owners of Meridian Life Partners, including Alpen Re UK</td></tr>
    </table>
  </div>
</section>

<!-- Page 4 -->
<section class="page p4">
  <div class="block" style="top:10px">
    <table class="role">
      <tr class="head"><td class="label">December 2012<br>to May 2013</td><td>Commercial &amp; MIS Advisor<br>Halden Life Limited</td></tr>
      <tr><td class="label">Role responsibilities:</td><td>
        <p>The primary objectives of the Commercial &amp; MIS Advisor / Manager are to;</p>
        <ol><li>1. Deliver commercial insights and advise the Senior Management Team regularly in all areas of the business including; Acquisition, the existing book (customers), financial performance, and the external environment</li>
        <li>2. Direct the development and implementation of Management Information Solutions and Systems for Halden Direct</li>
        <li>3. Direct the development of commercial modeling for Halden Direct including; Acquisition, Retention, Claims, Policy Administration, corporate overheads</li>
        <li>4. Produce reporting for the Executive regularly and as required</li>
        <li>5. Communicate the Financial statements to key stakeholders to inform future performance decisions</li>
        <li>6. Collaborating with strategic leaders who will contribute to the future growth of Halden Direct to ensure support is well placed to achieve corporate goals.</li></ol>
      </td></tr>
      <tr class="gap"><td class="label"></td><td></td></tr>
      <tr><td class="label">Reporting to:</td><td><p>Primary key stakeholders will be considered internal customers. Primary Customer Engagement will be with;</p></td></tr>
      <tr><td class="label">Key Relationships:</td><td>The Commercial Director<br>The Chief Customer Officer<br>Chief Marketing Officer</td></tr>
    </table>
    <table class="role">
      <tr class="head"><td class="label">July 2012<br>to December 2012</td><td>Head of Marketing Operations – Acquisition and Retention<br>Halden Life Limited</td></tr>
      <tr><td class="label">Role responsibilities:</td><td>
        <p>Primary responsibilities are to;</p>
        <ol><li>1. Collaborate with strategic leaders who will contribute to the future growth of Halden Direct</li>
        <li>2. Deliver commercial insights and recommendations in Acquisition planning, financial performance and the external environment</li>
        <li>3. Direct the development of commercial modeling for Acquisition and Retention</li>
        <li>4. Produce and communicate the Financial statements and supporting insights to inform future performance decisions</li>
        <li>5. Direct the management and implementation of reporting solutions for Halden Direct Acquisition and Retention</li>
        <li>6. Direct the implementation of projects impacting all aspects of Marketing</li></ol>
        <p style="margin-top:3px">The Head of Marketing Operations engages with senior leadership; delivering outcomes by influencing and leading others.</p>
      </td></tr>
      <tr><td class="label">Reporting to:<br>Key Relationships:</td><td>Chief Marketing Officer<br>New Ventures Director (formerly Joint Chief Operating Officer)<br>Commercial Director (formerly Joint Chief Operating Officer)<br>GM Call Centre Operations<br>Marketing Leadership Team<br>Head of Sales</td></tr>
    </table>
  </div>
</section>

<!-- Page 5 -->
<section class="page p5">
  <div class="block" style="top:10px">
    <table class="role">
      <tr class="head"><td class="label">October 2010<br>to July 2012</td><td>P&amp;L / Brand Manager – CoverWell<br>Part of the HARBOUR Group</td></tr>
      <tr><td class="label">Role responsibilities:</td><td>
        <p>The primary objectives of the P&amp;L / Brand Manager – CoverWell:</p>
        <ol><li>1. To deliver revenue to achieve CoverWell Direct growth objectives</li>
        <li>2. To manage costs to achieve CoverWell Direct profit objectives</li>
        <li>3. To actively drive strategic projects within CoverWell Direct, which contribute to either revenue or profit objectives, or both</li>
        <li>4. To contribute to the delivery of the revenue &amp; profit objectives of the Alliance partners</li>
        <li>5. To develop strategies for CoverWell and the broader Direct business, by understanding how CoverWell fits within HARBOUR Group</li>
        <li>6. Budget preparation, management monthly &amp; accountability</li>
        <li>7. Reporting of the P&amp;L</li>
        <li>8. Engage key internal stakeholders to ensure financial objectives are achieved</li></ol>
      </td></tr>
      <tr class="gap"><td class="label"></td><td></td></tr>
      <tr><td class="label">Reporting to:<br>Key Relationships:</td><td>Key stakeholder relationships with;<br>Three P&amp;L / Brand Managers – Alliance Partners<br>Two Joint CEO<br>Head of Sales<br>Head of Product<br>Head of Marketing</td></tr>
    </table>
    <table class="role">
      <tr class="head"><td class="label">January 2010<br>to October 2010</td><td>Product Portfolio Marketing Manager – CoverWell<br>Part of the HARBOUR Group</td></tr>
      <tr><td class="label">Role responsibilities:</td><td>
        <p>The primary objectives of the Product Portfolio Marketing Manager – CoverWell:</p>
        <ol><li>1. To deliver product life cycle management of current and future planned CoverWell products</li>
        <li>2. To direct the Marketing Managers and respective suppliers to achieve lead volumes at required cost metrics</li>
        <li>3. To actively manage a team of 4 Marketing Managers to achieve their objectives</li>
        <li>4. To communicate Marketing plans and objectives to key stakeholders within CoverWell, from Senior Management to Call Centre Managers</li>
        <li>5. To prepare short, medium, and long term budgets. Analyse each quarter, reforecast, and accountability</li></ol>
      </td></tr>
      <tr><td class="label">Reporting to:<br>Key Relationships:</td><td>Key stakeholder relationships with;<br>General Manager Marketing<br>Marketing Communications Manager<br>Digital Marketing Manager</td></tr>
    </table>
    <table class="role">
      <tr class="head"><td class="label">January 2008<br>to October 2010</td><td>Marketing Manager<br>CoverWell Pty Ltd</td></tr>
      <tr><td class="label">Role responsibilities</td><td>
        <p>The primary objectives of the Marketing Manager:</p>
        <ol><li>1. To Develop, monitor and implement acquisition strategy and plans including the introduction of new products cost effectively to market, inbound and outbound acquisition/upgrade/cross-sell activity</li></ol>
      </td></tr>
    </table>
  </div>
</section>

<!-- Page 6 -->
<section class="page p6">
  <div class="block" style="top:10px">
    <table class="role">
      <tr><td class="label"></td><td>
        <ol><li>2. Delivery of leads, profitability, product mix and channel targets by individual product and across the full product portfolio</li>
        <li>3. To develop and manage media strategy and new acquisition channel development to achieve leads and CPR requirements</li>
        <li>4. To identify and negotiate agreements with 3rd party channel partners for lead generation</li>
        <li>5. Manage all external media partners</li>
        <li>6. Report on marketing activity and results to the Senior Management team</li></ol>
      </td></tr>
      <tr class="gap"><td class="label"></td><td></td></tr>
      <tr><td class="label">Reporting to:<br>Key Relationships:</td><td>Key stakeholder relationships with;<br>General Manager, Acquisition<br>Marketing Communications Manager<br>Digital Marketing Manager<br>Senior Management Team</td></tr>
    </table>
  </div>
  <div class="pill" style="top:110px">
    For information on previous roles, please contact me at
    <svg width="5" height="4" viewBox="0 0 10 8" aria-hidden="true"><rect x=".5" y=".5" width="9" height="7" fill="none" stroke="#fff"/><path d="M.5 .5 L5 4.5 L9.5 .5" fill="none" stroke="#fff"/></svg>
    marisol.t@mailbox.example or <svg width="4" height="4" viewBox="0 0 10 10" aria-hidden="true"><path d="M2 1 L4 1 L5 3.5 L3.8 4.6 Q5 6.6 6 6.8 L7 5.6 L9.5 6.6 L9.5 8.6 Q9 9.6 7.6 9.4 Q1.5 8 .6 2.4 Q.6 1 2 1Z" fill="#fff"/></svg> 0400 118 263.
  </div>
  <div class="block" style="top:136px">
    <h2 class="section-title">QUALIFICATIONS</h2>
    <p class="sub">Degrees and Awards of relevance:</p>
    <table class="quals">
      <tr><th style="width:37%">Institution</th><th style="width:38%">Degree</th><th>Dates</th></tr>
      <tr><td>Coastal University of Technology</td><td>Bachelor of Business,<br>Major in Marketing and Small Business</td><td>January 1993<br>to June 1997</td></tr>
      <tr><td>CoverWell Pty Ltd</td><td>Employee of the Year<br>Award 2005</td><td>December 2005</td></tr>
      <tr><td>Halden Life Limited</td><td>Outstanding Achievement<br>Award 2009</td><td>December 2008</td></tr>
      <tr><td>Halden Life Limited</td><td>Overall Company Achievement<br>Award 2009</td><td>December 2009</td></tr>
    </table>
    <p class="sub" style="margin-top:14px">Executive Education:</p>
    <table class="quals">
      <tr><th style="width:37%">Institution</th><th style="width:38%">Program</th><th>Dates</th></tr>
      <tr><td>Halden Life Limited</td><td>Halden Senior Leaders Strategy Program</td><td>April 2012 to<br>Current</td></tr>
      <tr><td>Halden Life Limited</td><td>Equip Leadership Program</td><td>February 2009<br>to April 2010</td></tr>
      <tr><td>Southbank Academy</td><td>Certificate IV in Business,<br>Frontline Management</td><td>Completed<br>October 2008</td></tr>
    </table>
  </div>
  <div class="footer">- THANK YOU -</div>
</section>

</body>
</html>
```